KTV Catapult

I need a graphic package design for our new bodybuilding sports supplement. The artwork should be clean and useable for many formats. examples or great usage are www.brawnvelta.example, www.sinewcore.example and http://www.pellarynutrition.example/ as examples. I am adding our logo for your reference. The name Catapult is because it will help make "Big Guns" as a catch phrase, the product line will have other supplements such as creatine and protein powders and the artwork should be useable on all products. You can see our website for ideas at www.kestovalelabs.example
Updates

Hi everyone, There are some nice entries coming in. I do wonder if some of you are reading the brief as a few labels don't even highlight the product, KTV is the company, Catapult is the Product. Thanks Dex

Industry/Entity Type

Supplement

```html
<!DOCTYPE html>
<html lang="en">
<head>
<meta charset="utf-8">
<title>KTV Catapult – Label</title>
<link rel="stylesheet" href="https://fonts.googleapis.com/css2?family=Anton&family=Roboto+Condensed:wght@400;700&display=swap">
<style>
  :root {
    --page: #ffffff;
    --ink: #0b0b0b;
    --lime: #9cf52f;
    --lime-text: #8fe62a;
    --steel-light: #d6d6d6;
    --steel-mid: #a6a6a6;
    --steel-dark: #707070;
    --leaf-grey: #5c5c5c;
  }
  * { margin: 0; padding: 0; box-sizing: border-box; }
  html, body { width: 1200px; height: 1000px; overflow: hidden; background: var(--page); }
  .canvas { position: relative; width: 1200px; height: 1000px; font-family: "Roboto Condensed", Arial, sans-serif; }

  .label {
    position: absolute; left: 300px; top: 150px; width: 510px; height: 760px;
    border-radius: 28px; overflow: hidden;
    background: linear-gradient(90deg, var(--steel-dark) 0%, var(--steel-mid) 22%, var(--steel-light) 48%, var(--steel-mid) 78%, var(--steel-dark) 100%);
  }

  .swoosh-band {
    position: absolute; left: 0; top: 0; width: 510px; height: 170px;
    background: linear-gradient(180deg, var(--ink) 0%, var(--ink) 45%, var(--lime) 55%, var(--lime) 100%);
  }
  .leaf-accent {
    position: absolute; left: 320px; top: 215px; width: 180px; height: 185px;
    border-radius: 12px;
    background: linear-gradient(160deg, var(--leaf-grey) 0%, var(--leaf-grey) 30%, var(--lime) 70%);
  }

  .brand { position: absolute; left: 105px; top: 222px; width: 155px; color: var(--ink); font-weight: 700; text-align: center; }
  .brand-mark { font-size: 54px; line-height: 1; letter-spacing: 2px; }
  .brand-name { font-size: 12px; letter-spacing: 3px; margin-top: 6px; }

  .product-name {
    position: absolute; left: 0; right: 0; top: 408px; text-align: center;
    font-family: "Anton", Impact, sans-serif; font-size: 108px; line-height: 1;
    color: var(--ink); letter-spacing: 2px;
  }
  .tagline {
    position: absolute; left: 85px; top: 512px; width: 350px; height: 27px;
    background: var(--lime); color: var(--ink); font-weight: 700; font-size: 16.5px;
    display: flex; align-items: center; justify-content: center;
  }
  .benefits { position: absolute; left: 85px; top: 558px; list-style: none; }
  .benefits li {
    display: flex; align-items: center; gap: 10px; height: 22px;
    font-size: 12px; font-weight: 700; color: var(--ink);
  }
  .benefits svg { width: 14px; height: 10px; flex: none; }
  .claim { position: absolute; left: 0; right: 0; top: 662px; text-align: center; font-size: 16px; color: var(--ink); }
  .category { position: absolute; left: 0; right: 0; top: 692px; text-align: center; font-size: 20px; font-weight: 700; color: var(--lime-text); letter-spacing: 0.5px; }
</style>
</head>
<body>
<div class="canvas">
  <section class="label">
    <div class="swoosh-band" role="img" aria-label="Decorative black and lime swoosh band across the top of the label"></div>
    <div class="leaf-accent" role="img" aria-label="Decorative grey and lime leaf accent"></div>

    <div class="brand">
      <div class="brand-mark">KTV</div>
      <div class="brand-name">KESTOVALE LABS</div>
    </div>

    <h1 class="product-name">CATAPULT</h1>
    <div class="tagline">THE FIRST CHEWABLE STRENGTH ENHANCER</div>

    <ul class="benefits">
      <li><svg viewBox="0 0 14 10" aria-hidden="true"><path d="M1,9 L13,1" stroke="var(--lime)" stroke-width="3" stroke-linecap="round"/></svg>Increase Protein Synthesis while Reducing Protein Breakdown</li>
      <li><svg viewBox="0 0 14 10" aria-hidden="true"><path d="M1,9 L13,1" stroke="var(--lime)" stroke-width="3" stroke-linecap="round"/></svg>Increased Muscle Mass, Strength and Endurance</li>
      <li><svg viewBox="0 0 14 10" aria-hidden="true"><path d="M1,9 L13,1" stroke="var(--lime)" stroke-width="3" stroke-linecap="round"/></svg>Reduce Muscle Fatigue and Increase Blood Flow</li>
      <li><svg viewBox="0 0 14 10" aria-hidden="true"><path d="M1,9 L13,1" stroke="var(--lime)" stroke-width="3" stroke-linecap="round"/></svg>Increase Joint Range of Motion &amp; Decrease Joint Discomfort</li>
    </ul>

    <p class="claim">Clinically Studied Formula</p>
    <p class="category">DIETARY SUPPLEMENTS</p>
  </section>
</div>
</body>
</html>
```